Anzeigengestaltung für Steuerberater
Zielgruppe
aufgrund Unsimmitgkeiten mit pixelwerkhof.de, bitte ich Sie, diesen Event hier zu ignorieren.
Aufgabenstellung

```html
<!DOCTYPE html>
<html lang="de">
<head>
<meta charset="utf-8">
<title>Anzeige Steuerberatung – Neukunden-Gutschein</title>
<link rel="stylesheet" href="https://fonts.googleapis.com/css2?family=Montserrat:wght@600;700;800&display=swap">
<style>
  :root {
    --navy: #2b3656;
    --navy-deep: #1c2340;
    --orange: #e85f25;
    --orange-light: #f4a043;
    --white: #ffffff;
    --backdrop: #555555;
  }
  * { margin: 0; padding: 0; box-sizing: border-box; }
  html, body {
    width: 1200px; height: 1117px; overflow: hidden;
    background: var(--backdrop);
  }
  .ad {
    position: absolute; left: 94px; top: 167px;
    width: 1012px; height: 783px;
    background: var(--white);
    overflow: hidden;
    font-family: "Montserrat", Arial, sans-serif;
  }
  .top-band {
    position: absolute; left: 0; top: 0; width: 100%; height: 30px;
    background: linear-gradient(90deg, var(--navy) 0%, var(--navy) 29%, var(--orange) 64%, var(--orange) 100%);
  }
  .headline {
    position: absolute; left: 82px; top: 78px;
    font-weight: 700; font-size: 79px; line-height: 81px;
    color: var(--navy); letter-spacing: 0.5px;
  }
  .headline .accent { color: var(--orange); }
  .offer {
    position: absolute; left: 520px; top: 100px; width: 420px;
    text-align: center; color: var(--navy);
  }
  .offer-intro { font-weight: 700; font-size: 25px; line-height: 30px; }
  .offer-amount {
    font-weight: 800; font-size: 214px; line-height: 170px;
    color: var(--orange); letter-spacing: -4px; margin-top: 4px;
  }
  .offer-label { font-weight: 800; font-size: 47px; line-height: 45px; margin-top: 14px; }
  .photo {
    position: absolute; left: 0; top: 0; width: 1012px; height: 783px;
  }
  .slogan {
    position: absolute; left: 86px; top: 449px; width: 841px; height: 92px;
    border-radius: 46px; background: var(--orange);
    color: var(--white); font-weight: 700; font-size: 60px;
    display: flex; align-items: center; justify-content: center;
    letter-spacing: 1px;
    box-shadow: 0 6px 14px rgba(0,0,0,0.25);
  }
</style>
</head>
<body>
  <main class="ad">
    <div class="top-band"></div>

    <svg class="photo" viewBox="0 0 1012 783" role="img" aria-label="Foto: Hände tippen mit Stift auf einem Taschenrechner am Schreibtisch, blau-orange getönt">
      <defs>
        <linearGradient id="photo-tone" x1="0" y1="0" x2="1" y2="0.3">
          <stop offset="0" stop-color="#1c2340"/>
          <stop offset="0.3" stop-color="#3a3550"/>
          <stop offset="0.55" stop-color="#c8664a"/>
          <stop offset="0.8" stop-color="#f08a3a"/>
          <stop offset="1" stop-color="#e9541e"/>
        </linearGradient>
      </defs>
      <path d="M0 515 Q506 410 1012 518 L1012 783 L0 783 Z" fill="url(#photo-tone)"/>
    </svg>

    <h1 class="headline">
      <span class="accent">Vitamin C</span><br>
      für Ihre<br>
      Steuerer-<br>
      klärung
    </h1>

    <div class="offer">
      <p class="offer-intro">Profitieren Sie jetzt von Ihrem</p>
      <p class="offer-amount">30.-</p>
      <p class="offer-label">Neukunden-<br>Gutschein</p>
    </div>

    <div class="slogan">Einfach und erfrischend!</div>
  </main>
</body>
</html>
```